Corvane Web Site - Creating an Award-Winning Website

We need a simple but upscale web site designed in word press.
A new breed boutique Investment Bank. Specializing in select cutting-edge emerging growth company financings with a focus on impact investing.
This is a customer facing site that must instill confidence,be clean, streamline and easy to navigate.

Target Market(s)

Entrepreneurs, Finance professionals, Investors

Industry/Entity Type

Bank

Number of Pages Required

5+ page

Other font styles liked:
• see attached

Requirements
Must have
• Landing page
• About us
• Investors
• Entrepreneurs
• CrowdFunding
• Contact
Nice to have
• Sign up
• Similar look and feel to this site - https://pellandrow.com

```html
<!DOCTYPE html>
<html lang="en">
<head>
<meta charset="utf-8">
<title>Corvane Capital</title>
<link rel="stylesheet" href="https://fonts.googleapis.com/css2?family=Open+Sans:wght@300;400;600;700&family=Oswald:wght@400;500;600&display=swap">
<style>
:root{
  --blue:#2a7cc7;
  --blue-dark:#1f5f9e;
  --ink:#2f3338;
  --muted:#7a7f86;
  --line:#c9ced4;
  --band:#565656;
  --footer:#2b2f36;
  --white:#ffffff;
  --hero-a:#dfe9f3;
  --hero-b:#b7cde2;
}
*{box-sizing:border-box;margin:0;padding:0}
html,body{width:1200px;height:3920px;overflow:hidden}
body{font-family:"Open Sans",Arial,sans-serif;color:var(--ink);background:var(--white);position:relative}
.abs{position:absolute}
.btn{display:inline-block;background:var(--blue);color:var(--white);font-size:15px;font-weight:600;text-transform:uppercase;letter-spacing:.5px;padding:8px 26px}
.dots{display:flex;gap:12px;justify-content:center}
.dots span{width:14px;height:14px;border-radius:50%;background:var(--ink)}
.dots span.on{background:var(--blue)}
.arrow{font-size:54px;color:var(--ink);font-weight:300;line-height:1}

/* header */
.site-header{top:0;left:0;width:1200px;height:208px}
.brand{left:70px;top:20px;display:flex;flex-direction:column;align-items:center;width:260px}
.brand-mark{width:130px;height:130px;border-radius:50%;border:4px solid var(--blue)}
.brand-name{margin-top:8px;font-size:30px;font-weight:600;color:var(--blue);letter-spacing:1px}
.account{right:70px;top:58px;display:flex;gap:14px}
.account span{background:var(--ink);color:var(--white);font-size:13px;font-weight:600;padding:5px 12px}
.search{right:70px;top:102px;width:190px;height:32px;border:1px solid var(--line);font-size:13px;color:var(--muted);padding:6px 10px}
.main-nav{top:208px;left:0;width:1200px;height:42px;background:var(--blue);display:flex;justify-content:center;gap:6px}
.main-nav a{color:var(--white);font-size:15px;text-decoration:none;padding:10px 20px}
.main-nav a.active{background:var(--ink);font-weight:700;text-transform:uppercase}

/* hero */
.hero{top:250px;left:0;width:1200px;height:798px;background:linear-gradient(110deg,var(--hero-b),var(--hero-a) 45%,#eef3f8 70%,var(--hero-b))}
.hero-title{top:170px;width:100%;text-align:center;font-size:104px;font-weight:300;color:var(--blue);letter-spacing:3px}
.hero-mark{top:330px;left:540px;width:120px;height:120px;border-radius:50%;border:4px solid var(--blue)}
.hero-sub{top:515px;width:100%;text-align:center;font-size:28px;font-weight:600;color:var(--ink)}
.hero-text{top:560px;width:100%;text-align:center;font-size:17px;color:var(--ink)}
.hero-cta{top:600px;width:100%;text-align:center}
.hero .dots{top:745px;width:100%}
.hero .arrow.left{left:10px;top:360px}
.hero .arrow.right{right:10px;top:360px}

/* about */
.about{top:1048px;left:0;width:1200px;height:652px}
.about-mark{left:130px;top:172px;width:320px;height:320px;border-radius:50%;border:8px solid var(--ink);display:flex;align-items:center;justify-content:center;font-size:46px;font-weight:600;color:var(--blue)}
.about-copy{left:492px;top:228px;width:620px}
.about-copy h2{font-size:26px;font-weight:600;color:var(--blue);text-transform:uppercase;margin-bottom:18px}
.about-copy p{font-size:14px;line-height:1.6;color:var(--muted);margin-bottom:22px}

/* deals */
.deals{top:1700px;left:0;width:1200px;height:628px;background:var(--band)}
.deal{top:44px;width:328px;height:540px;background:var(--white)}
.deal-logo{height:180px;display:flex;align-items:center;justify-content:center;border-bottom:1px solid var(--line)}
.deal-logo span{width:150px;height:90px;background:#d9dce0}
.deal-logo span.round{width:90px;border-radius:50%;background:#cdd6df}
.deal-body{padding:20px 24px;text-align:center}
.deal-cat{font-size:13px;color:var(--muted);text-transform:uppercase;letter-spacing:1px}
.deal-name{font-family:"Oswald",Arial,sans-serif;font-size:30px;font-weight:600;color:var(--blue);text-transform:uppercase;margin:6px 0}
.deal-desc{font-size:13px;color:var(--muted);line-height:1.5;height:40px}
.deal-offer{font-size:15px;font-weight:700;margin:16px 0 18px}
.deal-stats{display:flex;justify-content:space-between;font-size:12px;color:var(--ink)}
.bar{height:14px;background:#e2e6ea;margin:6px 0}
.bar i{display:block;height:100%;background:var(--blue)}
.deal-meta{display:flex;justify-content:space-between;font-size:11px;color:var(--muted)}
.deal .btn{position:absolute;bottom:-12px;left:96px;font-size:14px;padding:6px 28px;text-transform:none}
.deals .arrow{color:var(--white);top:270px}

/* partners */
.partners{top:2400px;left:0;width:1200px;height:200px}
.partner-row{left:70px;top:60px;width:1060px;display:flex;justify-content:space-between}
.partner{font-size:38px;font-weight:600;color:var(--ink)}
.partners .arrow{top:52px;font-size:44px}
.partners .dots{top:180px;width:100%}

/* contact */
.contact{top:2640px;left:0;width:1200px;height:480px}
.contact h2{top:72px;width:100%;text-align:center;font-size:26px;font-weight:400;color:var(--blue);text-transform:uppercase}
.field{border:1px solid var(--line);font-size:14px;color:var(--ink);padding:9px 12px;background:var(--white)}
.field-row{top:150px;left:72px;width:1056px;display:flex;gap:24px}
.field-row .field{flex:1;height:44px}
.message{top:212px;left:72px;width:1056px;height:190px}
.send{top:418px;right:72px;width:250px;text-align:center}

/* testimonials */
.testimonials{top:3160px;left:0;width:1200px;height:400px;background:var(--blue)}
.testimonials h2{top:40px;width:100%;text-align:center;font-size:46px;font-weight:400;color:var(--white);text-transform:uppercase}
.testimonials h2 span{color:var(--ink)}
.testimonials .rule{top:110px;left:120px;width:960px;height:2px;background:rgba(255,255,255,.6)}
.portrait{left:80px;top:140px;width:164px;height:164px;border-radius:50%;border:6px solid var(--white);background:linear-gradient(160deg,#9fc6e6,#e9d5c2)}
.quote{left:280px;top:152px;width:840px;color:var(--white)}
.quote p{font-size:14px;line-height:1.55;margin-bottom:14px}
.quote b{display:block;font-size:14px}
.quote small{font-size:13px}
.testimonials .dots{top:340px;width:100%}
.testimonials .dots span{background:var(--ink)}
.testimonials .dots span.on{background:var(--white)}

/* footer */
.site-footer{top:3560px;left:0;width:1200px;height:360px;background:var(--footer);color:var(--white);text-align:center}
.social{top:56px;width:100%;display:flex;justify-content:center;gap:26px}
.social span{width:58px;height:58px;border-radius:50%;border:3px solid var(--white)}
.copy-title{top:150px;width:100%;font-size:38px;font-weight:400;text-transform:uppercase}
.copy-line{top:210px;width:100%;font-size:14px}
.copy-line a{color:var(--blue);text-decoration:none}
.to-top{top:278px;left:576px;width:48px;height:48px;border-radius:50%;background:var(--white)}
</style>
</head>
<body>

<header class="site-header abs">
  <div class="brand abs">
    <div class="brand-mark"></div>
    <div class="brand-name">CORVANE CAPITAL</div>
  </div>
  <div class="account abs"><span>LOGIN</span><span>SIGN UP</span></div>
  <div class="search abs">Search...</div>
</header>
<nav class="main-nav abs">
  <a class="active" href="#">Landing page</a><a href="#">About us</a><a href="#">Investors</a><a href="#">Entrepreneurs</a><a href="#">Crowdfunding</a><a href="#">Contact</a>
</nav>

<section class="hero abs" role="img" aria-label="Bright office scene with a person working at a desktop computer, washed in pale blue">
  <div class="arrow left abs">&#8249;&#8249;</div>
  <div class="arrow right abs">&#8250;&#8250;</div>
  <h1 class="hero-title abs">WELCOME</h1>
  <div class="hero-mark abs"></div>
  <div class="hero-sub abs">INVEST IN STARTUPS</div>
  <div class="hero-text abs">Get access to highly curated early and late stage investment opportunities</div>
  <div class="hero-cta abs"><span class="btn">Sign up for free</span></div>
  <div class="dots abs"><span class="on"></span><span></span><span></span><span></span></div>
</section>

<section class="about abs">
  <div class="about-mark abs">Corvane</div>
  <div class="about-copy abs">
    <h2>About our company</h2>
    <p>Our mission is to connect thoughtful investors with bold founders building companies that matter. We review hundreds of emerging growth businesses each year and select only a few for our members, with a clear focus on impact, transparency and long term value. Every offering is structured with care, documented in plain language and supported by our team from first look to final close, so investors and entrepreneurs can move forward with confidence.</p>
    <span class="btn" style="text-transform:none;font-size:13px;padding:6px 26px">Read More</span>
  </div>
</section>

<section class="deals abs">
  <div class="arrow abs" style="left:14px">&#8249;</div>
  <div class="arrow abs" style="right:14px">&#8250;</div>

  <article class="deal abs" style="left:72px">
    <div class="deal-logo"><span></span></div>
    <div class="deal-body">
      <div class="deal-cat">Restaurant &amp; Beverage</div>
      <div class="deal-name">Lonestar Kitchen</div>
      <div class="deal-desc">Coffee, bar and lounge with local dishes served in Austin</div>
      <div class="deal-offer">Offered by Northfield Ventures VC</div>
      <div class="deal-stats"><span>$48,287</span><span>Minimum</span></div>
      <div class="bar"><i style="width:38%"></i></div>
      <div class="deal-meta"><span>38% raised</span><span>21 days left</span></div>
    </div>
    <span class="btn">Read More</span>
  </article>

  <article class="deal abs" style="left:436px">
    <div class="deal-logo"><span></span></div>
    <div class="deal-body">
      <div class="deal-cat">Social Media</div>
      <div class="deal-name">Tunevault</div>
      <div class="deal-desc">Social marketplace for music collaboration and distribution</div>
      <div class="deal-offer">Offered by Northfield Ventures VC</div>
      <div class="deal-stats"><span>$121,396</span><span>380 Investors</span></div>
      <div class="bar"><i style="width:72%"></i></div>
      <div class="deal-meta"><span>72% raised</span><span>9 days left</span></div>
    </div>
    <span class="btn">Read More</span>
  </article>

  <article class="deal abs" style="left:800px">
    <div class="deal-logo"><span class="round"></span></div>
    <div class="deal-body">
      <div class="deal-cat">Distillery</div>
      <div class="deal-name">Harbor Distillers</div>
      <div class="deal-desc">Urban distillery and craft cocktail bar located on the harbor</div>
      <div class="deal-offer">Offered by Northfield Ventures VC</div>
      <div class="deal-stats"><span>$285,140</span><span>612 Investors</span></div>
      <div class="bar"><i style="width:86%"></i></div>
      <div class="deal-meta"><span>86% raised</span><span>4 days left</span></div>
    </div>
    <span class="btn">Read More</span>
  </article>
</section>

<section class="partners abs">
  <div class="arrow abs" style="left:14px">&#8249;</div>
  <div class="arrow abs" style="right:14px">&#8250;</div>
  <div class="partner-row abs">
    <span class="partner">Cellforge</span>
    <span class="partner">Genwave</span>
    <span class="partner">Tinderfox</span>
    <span class="partner">Paddlefold</span>
  </div>
  <div class="dots abs"><span class="on"></span><span></span><span></span><span></span></div>
</section>

<section class="contact abs">
  <h2 class="abs">Contact us</h2>
  <div class="field-row abs">
    <div class="field">First Name</div>
    <div class="field">Last Name</div>
    <div class="field">Contact no.</div>
    <div class="field">E-mail Address</div>
  </div>
  <div class="field message abs">Message</div>
  <span class="btn send abs">Send</span>
</section>

<section class="testimonials abs">
  <h2 class="abs">Satisfied <span>customers</span></h2>
  <div class="rule abs"></div>
  <div class="portrait abs" role="img" aria-label="Portrait of a smiling client family"></div>
  <div class="quote abs">
    <p>"Working with this team made our first private investment simple and clear. They explained every step, answered each question quickly and kept us informed long after closing. We now review every new offering they share and recommend them to friends who want to support growing companies with real impact in their communities."</p>
    <b>DANIEL MOREAU</b>
    <small>A Volunteer &amp; a Small Investor</small>
  </div>
  <div class="dots abs"><span class="on"></span><span></span><span></span><span></span></div>
</section>

<footer class="site-footer abs">
  <div class="social abs"><span></span><span></span><span></span><span></span></div>
  <div class="copy-title abs">Copyright</div>
  <div class="copy-line abs"><a href="https://pellandrow.com">Corvane Capital</a> &copy; 2024 Privacy Policy | Terms of use</div>
  <div class="to-top abs">
    <svg width="48" height="48" viewBox="0 0 48 48"><path d="M15 28 L24 19 L33 28" fill="none" stroke="#2b2f36" stroke-width="5"/></svg>
  </div>
</footer>

</body>
</html>
```